Harbourline Blinds & Shutters

It Needs to look classy as my target is the upper end of the blind market
I need a Logo design on front and description on back of what i do:
- Roller Blinds
- Vertical Blinds
- Venetian Blinds
- Plantation Shutters
- Aluminum External Shutters
and contact details
Declan
0418275063
and
Trent
0419852306
Updates
Hi Guys,
Sorry for the no feedback but i was waiting on my logo design. But its done now i have uploaded it. so if you could take a look and send through some designs
Reason: my logo was just finished an i just uploaded it today really dont understand why my deadline has been rached foe my bizcards as it states no deadline. But please extend
Target Market(s)
People that live on the coast and are looking for classy good quality blinds and shutters
Font styles to use
Other font styles liked:
- Copperplate Gothic,open to suggestion
Look and feel
Each slider illustrates characteristics of the customer's brand and the style your logo design should communicate.

```html
<!DOCTYPE html>
<html lang="en">
<head>
<meta charset="utf-8">
<title>Harbourline Blinds &amp; Shutters – Business Card</title>
<link href="https://fonts.googleapis.com/css2?family=Cinzel:wght@600&family=Arimo:wght@400&display=swap" rel="stylesheet">
<style>
  :root {
    --page: #e9e7e3;
    --card-dark: #1b1c1e;
    --card-mid: #2c2d30;
    --silver: #d9d6cf;
    --cream: #e8e0d0;
    --stripe-black: #111214;
    --text-light: #f2f2f2;
  }
  * { margin: 0; padding: 0; box-sizing: border-box; }
  html, body {
    width: 1200px; height: 855px; overflow: hidden;
    background: var(--page);
  }
  .canvas { position: relative; width: 1200px; height: 855px; }
  .card {
    position: absolute; top: 267px;
    width: 540px; height: 320px;
    border-radius: 22px; overflow: hidden;
    background: linear-gradient(135deg, var(--card-mid) 0%, var(--card-dark) 55%, #141517 100%);
    box-shadow: 0 10px 28px rgba(0,0,0,0.28);
  }
  .card--front { left: 45px; }
  .card--back { left: 615px; }

  /* Brand lockup: name plus one plain square */
  .brand {
    display: flex; align-items: center;
    font-family: "Cinzel", serif; font-weight: 600;
    color: var(--silver); line-height: 1;
  }
  .brand__mark { flex: none; background: var(--silver); }
  .brand__text { display: flex; flex-direction: column; }

  /* Front */
  .front-brand {
    position: absolute; left: 0; right: 0; top: 58px;
    justify-content: center; gap: 18px;
  }
  .front-brand .brand__mark { width: 58px; height: 58px; }
  .front-brand .brand__name { font-size: 38px; letter-spacing: 3px; }
  .front-brand .brand__tag { font-size: 14px; letter-spacing: 4px; margin-top: 10px; }
  .front-contacts {
    position: absolute; left: 0; right: 0; top: 188px;
    display: flex; justify-content: center;
    font-family: "Arimo", sans-serif; color: var(--text-light);
  }
  .contact { padding: 0 22px; text-align: center; }
  .contact + .contact { border-left: 1px solid var(--silver); }
  .contact__name { font-size: 20px; line-height: 1.2; }
  .contact__phone { font-size: 18px; letter-spacing: 1px; margin-top: 6px; }

  /* Back */
  .back-brand { position: absolute; left: 30px; top: 26px; gap: 8px; }
  .back-brand .brand__mark { width: 24px; height: 24px; }
  .back-brand .brand__name { font-size: 17px; letter-spacing: 1.5px; }
  .back-brand .brand__tag { font-size: 7px; letter-spacing: 1.8px; margin-top: 4px; }
  .services { position: absolute; right: 32px; top: 28px; text-align: right; }
  .services__title {
    font-family: "Cinzel", serif; font-weight: 600;
    font-size: 26px; letter-spacing: 2px; color: var(--silver);
    margin-bottom: 8px;
  }
  .services__list { list-style: none; font-family: "Arimo", sans-serif; color: var(--text-light); }
  .services__list li { font-size: 17px; line-height: 27px; }
  .back-decoration {
    position: absolute; left: 0; right: 0; bottom: 0; height: 100px;
    background: linear-gradient(160deg, var(--stripe-black) 0%, #6f6a61 45%, var(--cream) 100%);
  }
</style>
</head>
<body>
<main class="canvas">

  <section class="card card--front" aria-label="Card front">
    <div class="brand front-brand">
      <span class="brand__mark" aria-hidden="true"></span>
      <div class="brand__text">
        <span class="brand__name">HARBOURLINE</span>
        <span class="brand__tag">BLINDS &amp; SHUTTERS</span>
      </div>
    </div>
    <div class="front-contacts">
      <div class="contact">
        <div class="contact__name">Declan</div>
        <div class="contact__phone">0418275063</div>
      </div>
      <div class="contact">
        <div class="contact__name">Trent</div>
        <div class="contact__phone">0419852306</div>
      </div>
    </div>
  </section>

  <section class="card card--back" aria-label="Card back">
    <div class="back-decoration" role="img" aria-label="Decorative sweep of cream and black bands"></div>
    <div class="brand back-brand">
      <span class="brand__mark" aria-hidden="true"></span>
      <div class="brand__text">
        <span class="brand__name">HARBOURLINE</span>
        <span class="brand__tag">BLINDS &amp; SHUTTERS</span>
      </div>
    </div>
    <div class="services">
      <h2 class="services__title">SERVICES</h2>
      <ul class="services__list">
        <li>Roller Blinds</li>
        <li>Vertical Blinds</li>
        <li>Venetian Blinds</li>
        <li>Plantation Shutters</li>
        <li>Aluminum External Shutters</li>
      </ul>
    </div>
  </section>

</main>
</body>
</html>
```